Granite, Zinc and Clay Roofing LLC needs a new business card

I need a new business card because I have a new address.
I do slate copper and tile roofs. My webpage is: www.granitezincandclayroofing.example

```html
<!DOCTYPE html>
<html lang="en">
<head>
<meta charset="utf-8">
<title>Granite, Zinc &amp; Clay Roofing – Business Card</title>
<link rel="stylesheet" href="https://fonts.googleapis.com/css2?family=Poppins:wght@400;500;600&display=swap">
<style>
  :root {
    --page-bg: #dfe5ec;
    --card-bg: #eef1f4;
    --band-blue: #2f5f9c;
    --ink: #1b1d21;
    --ink-soft: #3a3d42;
  }
  * { box-sizing: border-box; margin: 0; padding: 0; }
  html, body {
    width: 1200px; height: 900px; overflow: hidden;
    background: var(--page-bg);
    font-family: "Poppins", sans-serif;
    color: var(--ink);
  }
  .business-card {
    position: absolute;
    left: 225px; top: 237px;
    width: 750px; height: 426px;
    background: var(--card-bg);
    overflow: hidden;
    box-shadow: 0 10px 30px rgba(30, 50, 80, 0.18);
  }
  .brand-band {
    position: absolute;
    left: 0; right: 0; top: 269px; bottom: 0;
    background: var(--band-blue);
    opacity: 0.85;
  }
  .contact-block {
    position: absolute;
    right: 27px; top: 29px;
    text-align: right;
  }
  .person-name { font-size: 21px; font-weight: 600; line-height: 26px; letter-spacing: 0.2px; }
  .person-role { font-size: 15px; font-weight: 400; line-height: 20px; color: var(--ink-soft); margin-top: 2px; }
  .divider {
    width: 46px; height: 3px; background: var(--ink);
    margin: 14px 0 0 auto;
  }
  .address { font-size: 18px; font-weight: 500; line-height: 26px; margin-top: 24px; }
  .web-lines { margin-top: 20px; }
  .web-line {
    display: flex; justify-content: flex-end; align-items: center; gap: 6px;
    font-size: 16px; font-weight: 500; line-height: 28px;
  }
  .web-line svg { width: 16px; height: 16px; fill: var(--ink); }
  .brand-rule {
    position: absolute;
    left: 97px; top: 332px;
    width: 422px; height: 3px;
    background: var(--ink);
  }
  .phone {
    position: absolute;
    right: 27px; top: 320px;
    display: flex; align-items: center; gap: 14px;
    font-size: 19px; font-weight: 600; line-height: 26px; letter-spacing: 0.5px;
  }
  .phone svg { width: 20px; height: 20px; fill: var(--ink); }
  .brand-mark {
    position: absolute;
    left: 100px; top: 347px;
    width: 20px; height: 20px;
    background: var(--ink);
  }
  .brand-name {
    position: absolute;
    left: 128px; top: 342px;
    font-size: 21px; font-weight: 500;
    line-height: 26px;
    color: var(--ink);
  }
</style>
</head>
<body>
  <main class="business-card">
    <div class="brand-band"></div>

    <section class="contact-block">
      <h1 class="person-name">Marek (Mark) Halden</h1>
      <p class="person-role">Owner</p>
      <div class="divider"></div>
      <p class="address">2870 Ridgeline Rd,<br>Fairbrook, OH 44390</p>
      <div class="web-lines">
        <p class="web-line">www.gzcroofing.example
          <svg viewBox="0 0 16 16" aria-hidden="true"><path d="M8 0a8 8 0 1 0 0 16A8 8 0 0 0 8 0zm5.9 7h-2.5a12 12 0 0 0-1-4.7A6 6 0 0 1 13.9 7zM8 2c.7.8 1.3 2.6 1.4 5H6.6C6.7 4.6 7.3 2.8 8 2zM5.6 2.3a12 12 0 0 0-1 4.7H2.1a6 6 0 0 1 3.5-4.7zM2.1 9h2.5a12 12 0 0 0 1 4.7A6 6 0 0 1 2.1 9zM8 14c-.7-.8-1.3-2.6-1.4-5h2.8c-.1 2.4-.7 4.2-1.4 5zm2.4-.3a12 12 0 0 0 1-4.7h2.5a6 6 0 0 1-3.5 4.7z"/></svg>
        </p>
        <p class="web-line">gzcroofingllc@example.com
          <svg viewBox="0 0 16 16" aria-hidden="true"><path d="M1 3h14v10H1V3zm1.6 1.5L8 8.6l5.4-4.1H2.6zM2.5 5.8v5.7h11V5.8L8 10 2.5 5.8z"/></svg>
        </p>
      </div>
    </section>

    <div class="brand-rule"></div>
    <div class="brand-mark" aria-hidden="true"></div>
    <p class="brand-name">Granite, Zinc &amp; Clay<br>Roofing</p>

    <p class="phone">
      <svg viewBox="0 0 24 24" aria-hidden="true"><path d="M6.6 10.8a15.1 15.1 0 0 0 6.6 6.6l2.2-2.2a1 1 0 0 1 1-.25 11.4 11.4 0 0 0 3.6.57 1 1 0 0 1 1 1V20a1 1 0 0 1-1 1A17 17 0 0 1 3 4a1 1 0 0 1 1-1h3.5a1 1 0 0 1 1 1c0 1.25.2 2.45.57 3.57a1 1 0 0 1-.25 1z"/></svg>
      (440) 555 0142
    </p>
  </main>
</body>
</html>
```